4D Hush Little Nest Luxury Ultrasound Billboard

Design a HIGH-END, MODERN billboard for my private prenatal ultrasound studio, 4D Hush Little Nest, located in Pace, Florida.
This billboard will be viewed by drivers traveling at highway speeds, so it must be extremely clean, simple, and readable within 6 seconds.
About My Business
4D Hush Little Nest is a private prenatal ultrasound studio specializing in:
Highest technology 4D/HD Ultrasounds
Early Gender Determination
Pregnancy Confirmation
I have been serving families for nearly 10 years and is known for creating a memorable experience, not just an ultrasound appointment.
Design Style
I DO NOT want:
Flowers
Leaves
Swirls
Glitter
Hearts everywhere
Busy backgrounds
Generic maternity stock graphics
I DO want:
Modern
Luxury
Upscale
Clean
Professional
Eye-catching
Premium medical spa feel
Colors
Use colors from my logo:
LOGO Green ( or a deep green)
Black
White
Soft Gold accents
Images:
Incorporate my professional headshot in a clean, modern way, logo, and the ultrasound images
Text
Keep wording minimal.
Primary Headline ( OPEN TO IDEAS) :
EXAMPLES ( WOULD RATHER SOMETHING MORE CATCHY)
" ADVANCED IMAGING. UNFORGETTABLE MOMENTS"
"MEET YOUR BABY BEFORE BIRTH"
Under headline:
4D Ultrasound • Early Gender • Pregnancy Confirmation
Business Name:
4D Hush Little Nest
Private Prenatal Ultrasound Studio
Phone Number:
850-471-3905
Important
This billboard must be readable in 5–6 seconds from a moving vehicle.
Less text is better.
The phone number and business name must be visible from a distance.
The design should feel like a premium brand that immediately tells expecting parents:
“This is where I go to see my baby.”
Files Provided
Official logo
Headshot
Ultrasound images
Don’t make this look like a medical office billboard.
Make it look like a luxury baby experience billboard. That’s what separates 4D Hush Little Nest from hospitals, OB offices, and all the new studios popping up around you. The emotional connection is what gets moms to book. ❤️
Billboard Size - 10.6” x 36”

```html
<!DOCTYPE html>
<html lang="en">
<head>
<meta charset="utf-8">
<title>4D Hush Little Nest – Billboard</title>
<link rel="stylesheet" href="https://fonts.googleapis.com/css2?family=Anton&family=Oswald:wght@500;600;700&display=swap">
<style>
  :root {
    --page-bg-center: #ffffff;
    --page-bg-edge: #d5dde6;
    --cream-light: #f6eee4;
    --cream: #eadbc8;
    --band: #3d4144;
    --bronze: #8c7257;
    --bronze-light: #b9825c;
    --ink: #1f1a17;
    --cocoa: #4f4034;
    --taupe: #6f5a48;
    --white: #ffffff;
    --sage: #5c6b5d;
  }
  * { box-sizing: border-box; margin: 0; padding: 0; }
  html, body {
    width: 1200px; height: 1200px; overflow: hidden;
    background: radial-gradient(circle at 50% 50%, var(--page-bg-center) 0%, var(--page-bg-edge) 100%);
  }
  .stage { position: relative; width: 1200px; height: 1200px; }

  .pole {
    position: absolute; left: 581px; top: 446px; width: 68px; height: 203px;
    background: var(--band);
  }

  .billboard {
    position: absolute;
    width: 1740px; height: 512px;
    transform: scale(0.6207); transform-origin: top left;
    background: linear-gradient(100deg, var(--cream) 0%, var(--cream-light) 45%, var(--cream) 100%);
    overflow: hidden;
  }
  .billboard--mounted { left: 55px; top: 129px; }
  .billboard--flat { left: 60px; top: 736px; }

  .info-band {
    position: absolute; left: 0; top: 385px; width: 1740px; height: 127px;
    background: var(--band);
  }

  .photo { position: absolute; }
  .photo--owner {
    left: 42px; top: 12px; width: 320px; height: 500px;
    border-radius: 140px 140px 0 0;
    background: linear-gradient(180deg, #d8c3a0 0%, #c9a98a 35%, #3f5a40 60%, #2f4a33 100%);
  }
  .photo--scanner {
    left: 1232px; top: 110px; width: 255px; height: 275px;
    border-radius: 10px;
    background: linear-gradient(180deg, #2a2a2c 0%, #6b3a2c 30%, #8b4c38 50%, #3a3a3c 70%, #b5b5b5 100%);
  }
  .photo--parents {
    left: 1482px; top: 0; width: 258px; height: 385px;
    background: linear-gradient(160deg, #d9c8b4 0%, #8ea3b4 35%, #cdb9a2 60%, #5c4a3e 100%);
  }

  .brand-card {
    position: absolute; left: 22px; top: 398px; width: 190px; height: 92px;
    background: var(--white); border: 2px solid #cfcfcf; border-radius: 10px;
    display: flex; flex-direction: column; align-items: center; justify-content: center; gap: 4px;
    text-align: center;
  }
  .brand-card__name {
    font-family: "Oswald", sans-serif; font-weight: 600; font-size: 21px;
    line-height: 1.05; color: var(--sage); padding: 0 8px;
  }
  .brand-card__tag {
    font-family: "Oswald", sans-serif; font-weight: 600; font-size: 10px;
    letter-spacing: 0.5px; color: var(--sage);
  }

  .outlined {
    text-shadow:
      2px 0 0 var(--white), -2px 0 0 var(--white), 0 2px 0 var(--white), 0 -2px 0 var(--white),
      2px 2px 0 var(--white), -2px -2px 0 var(--white), 2px -2px 0 var(--white), -2px 2px 0 var(--white);
  }

  .services {
    position: absolute; left: 337px; top: 26px; width: 1240px;
    display: flex; gap: 16px; white-space: nowrap;
    font-family: "Oswald", sans-serif; font-weight: 700; font-size: 46px; line-height: 60px;
    color: var(--ink);
  }
  .services__item::before {
    content: ""; display: inline-block; width: 6px; height: 36px;
    background: var(--bronze); margin-right: 14px; vertical-align: -2px;
  }

  .headline {
    position: absolute; left: 365px; top: 100px; width: 860px;
    font-family: "Anton", sans-serif; font-weight: 400; font-size: 102px; line-height: 120px;
    white-space: nowrap; letter-spacing: -1px;
  }
  .headline .w1 { color: var(--cocoa); }
  .headline .w2 { color: #6d5645; }
  .headline .w3 { color: #8e6a4f; }
  .headline .w4 { color: var(--bronze-light); }

  .tagline {
    position: absolute; left: 344px; width: 900px; text-align: center;
    font-family: "Oswald", sans-serif; font-weight: 600; color: var(--taupe);
    white-space: nowrap; letter-spacing: -0.5px;
  }
  .tagline--first { top: 238px; font-size: 42px; line-height: 54px; }
  .tagline--second { top: 292px; font-size: 55px; line-height: 68px; color: var(--cocoa); }

  .phone-icon { position: absolute; left: 367px; top: 407px; width: 80px; height: 80px; }
  .phone-number {
    position: absolute; left: 457px; top: 390px;
    font-family: "Anton", sans-serif; font-size: 97px; line-height: 110px;
    color: var(--white); letter-spacing: 1px; white-space: nowrap;
  }
  .studio-pill {
    position: absolute; left: 1019px; top: 409px; width: 691px; height: 75px;
    border-radius: 40px; background: var(--bronze);
    display: flex; align-items: center; justify-content: center;
    font-family: "Oswald", sans-serif; font-weight: 600; font-size: 46px;
    color: var(--white); white-space: nowrap; letter-spacing: -0.5px;
  }
</style>
</head>
<body>
<main class="stage">
  <div class="pole" aria-hidden="true"></div>

  <section class="billboard billboard--mounted" aria-label="4D Hush Little Nest billboard on post">
    <div class="info-band"></div>
    <div class="photo photo--owner" role="img" aria-label="Portrait of the studio owner in green scrubs holding an ultrasound probe"></div>
    <div class="photo photo--scanner" role="img" aria-label="Ultrasound machine displaying a 4D baby scan"></div>
    <div class="photo photo--parents" role="img" aria-label="Smiling expecting couple, hands on the pregnant belly"></div>
    <div class="brand-card">
      <span class="brand-card__name">4D Hush Little Nest</span>
      <span class="brand-card__tag">PRENATAL ULTRASOUND STUDIO</span>
    </div>
    <p class="services outlined">
      <span class="services__item">4D ULTRASOUND</span>
      <span class="services__item">EARLY GENDER</span>
      <span class="services__item">PREGNANCY CONFIRMATION</span>
    </p>
    <h1 class="headline outlined">
      <span class="w1">SEE</span> <span class="w2">YOUR</span> <span class="w3">BABY</span> <span class="w4">SOONER</span>
    </h1>
    <p class="tagline tagline--first outlined">" ADVANCED IMAGING.UNFORGETTABLE MOMENTS"</p>
    <p class="tagline tagline--second outlined">"MEET YOUR BABY BEFORE BIRTH”</p>
    <svg class="phone-icon" viewBox="0 0 80 80" aria-hidden="true">
      <circle cx="40" cy="40" r="40" fill="var(--bronze)"/>
      <path d="M30 20 h10 l3 12 -7 5 q3 9 10 14 l6-6 12 4 v10 q-2 6 -9 6 q-18 -2 -28 -20 q-7 -14 -3 -25 z"
            fill="var(--band)" transform="rotate(10 40 40)"/>
    </svg>
    <p class="phone-number">850-471-3905</p>
    <div class="studio-pill">Private Prenatal Ultrasound Studio</div>
  </section>

  <section class="billboard billboard--flat" aria-label="4D Hush Little Nest billboard, flat view">
    <div class="info-band"></div>
    <div class="photo photo--owner" role="img" aria-label="Portrait of the studio owner in green scrubs holding an ultrasound probe"></div>
    <div class="photo photo--scanner" role="img" aria-label="Ultrasound machine displaying a 4D baby scan"></div>
    <div class="photo photo--parents" role="img" aria-label="Smiling expecting couple, hands on the pregnant belly"></div>
    <div class="brand-card">
      <span class="brand-card__name">4D Hush Little Nest</span>
      <span class="brand-card__tag">PRENATAL ULTRASOUND STUDIO</span>
    </div>
    <p class="services outlined">
      <span class="services__item">4D ULTRASOUND</span>
      <span class="services__item">EARLY GENDER</span>
      <span class="services__item">PREGNANCY CONFIRMATION</span>
    </p>
    <h2 class="headline outlined">
      <span class="w1">SEE</span> <span class="w2">YOUR</span> <span class="w3">BABY</span> <span class="w4">SOONER</span>
    </h2>
    <p class="tagline tagline--first outlined">" ADVANCED IMAGING.UNFORGETTABLE MOMENTS"</p>
    <p class="tagline tagline--second outlined">"MEET YOUR BABY BEFORE BIRTH”</p>
    <svg class="phone-icon" viewBox="0 0 80 80" aria-hidden="true">
      <circle cx="40" cy="40" r="40" fill="var(--bronze)"/>
      <path d="M30 20 h10 l3 12 -7 5 q3 9 10 14 l6-6 12 4 v10 q-2 6 -9 6 q-18 -2 -28 -20 q-7 -14 -3 -25 z"
            fill="var(--band)" transform="rotate(10 40 40)"/>
    </svg>
    <p class="phone-number">850-471-3905</p>
    <div class="studio-pill">Private Prenatal Ultrasound Studio</div>
  </section>
</main>
</body>
</html>
```